Business Card Design

I need a bussiness card that have some picture of a van and lorry.
Updates

Hello I could ask you to print business cards and message to the home address?

Industry/Entity Type

Business

Contact Information for Business Card

K&M Transport LTD
truck and vans fridge
drivers recruitment
k.m-transport@quillmail.example
tel nr 07831452096

```html
<!DOCTYPE html>
<html lang="en">
<head>
<meta charset="utf-8">
<title>K&amp;M Transport LTD – Business Card</title>
<link href="https://fonts.googleapis.com/css2?family=Exo+2:wght@700&family=Open+Sans:wght@400&display=swap" rel="stylesheet">
<style>
  :root {
    --backdrop: #ececec;
    --charcoal: #3d3d3f;
    --charcoal-deep: #323234;
    --lime: #8cc63f;
    --lime-light: #9fd14f;
    --sky-top: #5d7ea6;
    --sky-mid: #b9cbe0;
    --road: #6d7278;
    --silver: #d9dcdf;
    --ink-light: #ffffff;
    --ink-muted: #e4e4e4;
  }
  * { margin: 0; padding: 0; box-sizing: border-box; }
  html, body {
    width: 1200px; height: 1000px; overflow: hidden;
    background: var(--backdrop);
  }
  .sheet { position: relative; width: 1200px; height: 1000px; }
  .card {
    position: absolute; left: 215px; width: 770px; height: 440px;
    border-radius: 40px; overflow: hidden;
    box-shadow: 0 10px 28px rgba(0,0,0,0.18);
  }
  .card--front { top: 40px; }
  .card--back { top: 520px; }
  .card__art { position: absolute; inset: 0; width: 770px; height: 440px; display: block; }

  .company-name {
    position: absolute;
    font-family: "Exo 2", sans-serif; font-weight: 700;
    color: var(--ink-light); letter-spacing: 0.5px; white-space: nowrap;
  }
  .card--front .company-name { left: 70px; top: 318px; font-size: 34px; }
  .card--back .company-name { left: 510px; top: 200px; font-size: 26px; }

  .services {
    position: absolute; left: 510px; top: 248px;
    font-family: "Open Sans", sans-serif; font-size: 17px; line-height: 28px;
    color: var(--ink-light); list-style: none;
  }

  .contact {
    position: absolute; left: 55px; top: 95px; list-style: none;
    font-family: "Open Sans", sans-serif; font-size: 17px; color: var(--ink-muted);
  }
  .contact__item { display: flex; align-items: center; gap: 16px; height: 36px; white-space: nowrap; }
  .contact__icon { width: 20px; height: 20px; flex: none; }
</style>
</head>
<body>
<main class="sheet">

  <section class="card card--front" aria-label="Business card front">
    <svg class="card__art" viewBox="0 0 770 440">
      <defs>
        <linearGradient id="photo-tones" x1="0" y1="0" x2="0" y2="1">
          <stop offset="0" stop-color="var(--sky-top)"/>
          <stop offset="0.45" stop-color="var(--sky-mid)"/>
          <stop offset="0.6" stop-color="#8d949b"/>
          <stop offset="1" stop-color="var(--road)"/>
        </linearGradient>
      </defs>
      <rect class="card__base" width="770" height="440" fill="var(--charcoal)"/>
      <path class="card__photo" role="img" aria-label="Photo of two vans driving on a road under a bright sky"
            d="M440,0 L770,0 L770,440 L250,440 C268,260 340,90 440,0 Z" fill="url(#photo-tones)"/>
      <path class="card__swoosh" d="M440,0 C340,90 268,260 250,440" fill="none" stroke="var(--silver)" stroke-width="6" opacity="0.85"/>
      <rect class="card__name-tab" x="50" y="304" width="370" height="64" rx="32" fill="var(--charcoal-deep)"/>
      <rect class="card__edge" x="0" y="434" width="770" height="6" fill="var(--lime)"/>
    </svg>
    <p class="company-name">K&amp;M Transport LTD</p>
  </section>

  <section class="card card--back" aria-label="Business card back">
    <svg class="card__art" viewBox="0 0 770 440" aria-hidden="true">
      <rect width="770" height="440" fill="var(--charcoal)"/>
      <path class="card__band-outer" d="M640,0 L770,0 L770,440 L380,440 C405,250 495,90 640,0 Z" fill="var(--lime-light)"/>
      <path class="card__band-gap" d="M665,0 L770,0 L770,440 L405,440 C430,250 520,88 665,0 Z" fill="var(--charcoal)"/>
      <path class="card__panel" d="M685,0 L770,0 L770,440 L425,440 C450,250 537,92 685,0 Z" fill="var(--lime)"/>
    </svg>

    <ul class="contact">
      <li class="contact__item">
        <svg class="contact__icon" viewBox="0 0 22 22" aria-hidden="true">
          <rect x="6" y="2" width="10" height="18" rx="2" fill="none" stroke="var(--ink-muted)" stroke-width="1.6"/>
          <line x1="9.5" y1="17" x2="12.5" y2="17" stroke="var(--ink-muted)" stroke-width="1.4"/>
        </svg>
        <span>07831452096</span>
      </li>
      <li class="contact__item">
        <svg class="contact__icon" viewBox="0 0 22 22" aria-hidden="true">
          <rect x="2" y="5" width="18" height="12" fill="none" stroke="var(--ink-muted)" stroke-width="1.6"/>
          <path d="M2,5 L11,12 L20,5" fill="none" stroke="var(--ink-muted)" stroke-width="1.6"/>
        </svg>
        <span>k.m-transport@quillmail.example</span>
      </li>
    </ul>

    <p class="company-name">K&amp;M Transport LTD</p>
    <ul class="services">
      <li>fridge drivers recruitment</li>
      <li>truck and vans</li>
    </ul>
  </section>

</main>
</body>
</html>
```